Design for a 3-4 screens mobile app

The app is a "simple" ordering mobile app.
1. START screen : user can select either "NEW order" either "VIEW history" - or, can access the usual Contact, About, and Conditions pages.
2. NEW order : is a sequence of 3 basic screens/forms made of 3-4 fields each. Logic is the following: you select the service you need, its recurrence, mention where you are located and then you post it towards the marketplace...
3. VIEW history : is where you land at the end of the ordering process - and accessible from START screen. You see there your previous orders, and their statuses.
Mandatory : we need design for START screen, NEW order and VIEW history screens.
Design but be optimized for Smartphones, used in Portrait mode.
Please take into account the design of the website promoting the Mobile App: https://tidyvanlane.be/
Optional but of course nice to have if you could propose some design or guidance for Contact, About, and Conditions pages...
Here attached a full screen sequence.
Updates
Thanks for all your proposals ! They were submitted to the final customer, he selects one ASAP !
Number of Pages Required
3 page
Look and feel
Each slider illustrates characteristics of the customer's brand and the style your logo design should communicate.

```html
<!DOCTYPE html>
<html lang="en">
<head>
<meta charset="utf-8">
<title>Tidy Van Lane – Start</title>
<link rel="stylesheet" href="https://fonts.googleapis.com/css2?family=Raleway:wght@500&family=Roboto:wght@400;500;700&display=swap">
<style>
  :root {
    --orange: #ff6c05;
    --ink: #2b2b2b;
    --tile: #2f2f2f;
    --footer: #3b3b3b;
    --footer-dark: #2c2c2c;
    --white: #ffffff;
    --mascot: #f4b24a;
  }
  * { margin: 0; padding: 0; box-sizing: border-box; }
  html, body { width: 667px; height: 1200px; overflow: hidden; }
  body {
    background: var(--orange);
    font-family: "Roboto", Arial, sans-serif;
    color: var(--white);
    position: relative;
  }
  .top-bar {
    position: absolute; top: 10px; left: 24px; right: 24px; height: 52px;
    display: flex; justify-content: space-between; align-items: center;
  }
  .icon-box {
    width: 52px; height: 52px; background: var(--ink);
    border: 2px solid var(--white); border-radius: 6px;
    display: flex; align-items: center; justify-content: center;
  }
  .social { display: flex; gap: 4px; }
  .social .icon-box { border-radius: 4px; }
  .social-dot { width: 14px; height: 14px; border-radius: 50%; background: var(--white); }
  .brand {
    position: absolute; top: 110px; left: 70px;
    display: flex; align-items: center; gap: 18px;
  }
  .brand-mascot {
    width: 130px; height: 200px; border-radius: 18px;
    background: linear-gradient(180deg, var(--mascot), #5aa9c8);
  }
  .brand-name {
    font-family: "Raleway", Arial, sans-serif; font-weight: 500;
    font-size: 44px; color: var(--white); white-space: nowrap;
  }
  .welcome {
    position: absolute; top: 400px; left: 50px; right: 50px;
    text-align: center; font-size: 22px; line-height: 30px;
  }
  .contact-row {
    position: absolute; left: 0; right: 0;
    display: flex; justify-content: center; gap: 40px;
    font-size: 20px; align-items: center;
  }
  .contact-row span { display: inline-flex; align-items: center; gap: 10px; }
  .contact-row.phone-mail { top: 492px; }
  .contact-row.site { top: 542px; }
  .actions {
    position: absolute; top: 712px; left: 86px; right: 90px;
    display: flex; justify-content: space-between;
  }
  .action-tile {
    width: 184px; height: 182px; background: var(--tile); border-radius: 8px;
    display: flex; flex-direction: column; align-items: center; justify-content: center; gap: 18px;
    font-weight: 700; font-size: 22px; white-space: nowrap;
  }
  .footer-links {
    position: absolute; top: 1080px; left: 0; right: 0; height: 64px;
    background: var(--footer); display: flex; justify-content: center; align-items: center; gap: 40px;
    font-size: 17px;
  }
  .copyright {
    position: absolute; top: 1144px; left: 0; right: 0; bottom: 0;
    background: var(--footer-dark); display: flex; justify-content: center; align-items: center;
    font-size: 15px;
  }
</style>
</head>
<body>
  <header class="top-bar">
    <div class="icon-box menu-button">
      <svg width="30" height="24" viewBox="0 0 30 24"><g fill="#fff"><rect y="1" width="30" height="4" rx="1"/><rect y="10" width="30" height="4" rx="1"/><rect y="19" width="30" height="4" rx="1"/></g></svg>
    </div>
    <nav class="social">
      <div class="icon-box" aria-label="Social page"><span class="social-dot"></span></div>
      <div class="icon-box" aria-label="Social feed"><span class="social-dot"></span></div>
      <div class="icon-box">
        <svg width="26" height="26" viewBox="0 0 24 24"><path fill="#fff" d="M6.6 10.8a15.1 15.1 0 0 0 6.6 6.6l2.2-2.2c.3-.3.7-.4 1-.2 1.1.4 2.3.6 3.6.6.6 0 1 .4 1 1V20c0 .6-.4 1-1 1A17 17 0 0 1 3 4c0-.6.4-1 1-1h3.5c.6 0 1 .4 1 1 0 1.3.2 2.5.6 3.6.1.3 0 .7-.2 1z"/></svg>
      </div>
      <div class="icon-box">
        <svg width="30" height="22" viewBox="0 0 30 22"><rect x="1.5" y="1.5" width="27" height="19" fill="none" stroke="#fff" stroke-width="2.5"/><path d="M2 2l13 10 13-10" fill="none" stroke="#fff" stroke-width="2.5"/></svg>
      </div>
    </nav>
  </header>

  <div class="brand">
    <div class="brand-mascot" role="img" aria-label="Mascot illustration of a cheerful cleaner with a bucket"></div>
    <div class="brand-name">Tidy Van Lane</div>
  </div>

  <p class="welcome">Welcome on Tidy Van Lane, should you have any question about this App or our services, do not hesitate to</p>

  <div class="contact-row phone-mail">
    <span>
      <svg width="20" height="20" viewBox="0 0 24 24"><path fill="none" stroke="#fff" stroke-width="2" d="M6.6 10.8a15.1 15.1 0 0 0 6.6 6.6l2.2-2.2c.3-.3.7-.4 1-.2 1.1.4 2.3.6 3.6.6.6 0 1 .4 1 1V20c0 .6-.4 1-1 1A17 17 0 0 1 3 4c0-.6.4-1 1-1h3.5c.6 0 1 .4 1 1 0 1.3.2 2.5.6 3.6.1.3 0 .7-.2 1z"/></svg>
      +32 470 12 34 56
    </span>
    <span>
      <svg width="24" height="18" viewBox="0 0 24 18"><rect x="1" y="1" width="22" height="16" fill="none" stroke="#fff" stroke-width="2"/><path d="M1 1l11 8 11-8" fill="none" stroke="#fff" stroke-width="2"/></svg>
      info@tidyvanlane.be
    </span>
  </div>
  <div class="contact-row site">
    <span>
      <svg width="22" height="22" viewBox="0 0 24 24"><g fill="none" stroke="#fff" stroke-width="2"><circle cx="12" cy="12" r="10"/><ellipse cx="12" cy="12" rx="4.5" ry="10"/><path d="M2 12h20"/></g></svg>
      www.tidyvanlane.be
    </span>
  </div>

  <main class="actions">
    <div class="action-tile new-order">
      <svg width="78" height="78" viewBox="0 0 78 78"><g fill="none" stroke="#fff" stroke-width="4"><circle cx="39" cy="39" r="36"/><path d="M39 18v42M18 39h42"/></g></svg>
      New Order
    </div>
    <div class="action-tile view-history">
      <svg width="78" height="78" viewBox="0 0 78 78"><g fill="none" stroke="#fff" stroke-width="3.5"><rect x="14" y="6" width="40" height="58" rx="3"/><path d="M22 6v-2M30 6v-2M38 6v-2M46 6v-2M22 22h24M22 32h24M22 42h14"/><circle cx="54" cy="56" r="14" fill="#2f2f2f"/><path d="M54 48v9h7"/></g></svg>
      View History
    </div>
  </main>

  <footer>
    <nav class="footer-links"><span>About</span><span>Contact</span><span>Terms of Use</span></nav>
    <div class="copyright">© Copyright 2017 Tidy Van Lane. All Rights Reserved.</div>
  </footer>
</body>
</html>
```